Business Card Design Project

We are a commercial talent casting company, a very "now" company. We need a new business card that is both current, graphic and elegantly interesting. As we are a service business,
we need something that will attract the attention of new clients,
yet project a business that is 25 years old.

Industry/Entity Type

Business

Requirements
Must have
• 1. Logo - Nora Quillan Casting
2. Address - 47 Thornbury Street
New York, New York 10010
3. Phone - 212-738-4192
4. E-Mail - Casting@noraquillan.example

Nice to have
• Would like the card in black and white with the only accent
color being red.

```html
<!DOCTYPE html>
<html lang="en">
<head>
<meta charset="utf-8">
<title>Nora Quillan Casting — Business Card</title>
<link rel="stylesheet" href="https://fonts.googleapis.com/css2?family=Arimo:wght@400;700&family=Cinzel:wght@400&display=swap">
<style>
  :root {
    --stage: #d9d9d9;
    --paper: #ffffff;
    --ink: #000000;
    --accent: #e0161b;
    --reverse: #ffffff;
  }
  html, body {
    margin: 0;
    padding: 0;
    width: 1200px;
    height: 786px;
    overflow: hidden;
    background: var(--stage);
  }
  .canvas {
    position: relative;
    width: 1200px;
    height: 786px;
    background: var(--stage);
  }
  .card {
    position: absolute;
    left: 119px;
    top: 83px;
    width: 957px;
    height: 586px;
    background: var(--paper);
    overflow: hidden;
  }
  .card__wave {
    position: absolute;
    left: 0;
    top: 0;
    width: 957px;
    height: 586px;
  }
  .wave-fill { fill: var(--ink); }
  .wave-edge { fill: none; stroke: var(--accent); stroke-width: 5; }

  .company-name {
    position: absolute;
    left: 224px;
    top: 148px;
    margin: 0;
    font-family: "Cinzel", serif;
    font-weight: 400;
    font-size: 41px;
    line-height: 41px;
    letter-spacing: 1px;
    color: var(--ink);
    white-space: nowrap;
  }
  .brand-mark {
    position: absolute;
    left: 212px;
    top: 520px;
    display: flex;
    align-items: center;
    gap: 10px;
    margin: 0;
    font-family: "Arimo", sans-serif;
    font-weight: 400;
    font-size: 30px;
    line-height: 34px;
    color: var(--accent);
    white-space: nowrap;
  }
  .brand-mark__square {
    width: 22px;
    height: 22px;
    background: var(--accent);
  }
  .contact {
    position: absolute;
    left: 600px;
    top: 471px;
    width: 460px;
    text-align: center;
    font-family: "Arimo", sans-serif;
    color: var(--reverse);
    font-style: normal;
  }
  .contact__name {
    font-size: 41px;
    line-height: 44px;
  }
  .contact__line {
    font-size: 28px;
    line-height: 33px;
    white-space: nowrap;
  }
</style>
</head>
<body>
<div class="canvas">
  <div class="card">
    <svg class="card__wave" viewBox="0 0 1067 653" preserveAspectRatio="none" aria-hidden="true">
      <path class="wave-fill" d="M0,500 C80,580 200,612 330,578 C500,532 600,412 800,357 C900,331 1000,340 1067,352 L1067,653 L0,653 Z"/>
      <path class="wave-edge" d="M0,500 C80,580 200,612 330,578 C500,532 600,412 800,357 C900,331 1000,340 1067,352"/>
    </svg>
  </div>

  <h1 class="company-name">Nora Quillan Casting</h1>
  <p class="brand-mark"><span class="brand-mark__square"></span>Nora Quillan</p>

  <address class="contact">
    <div class="contact__name">Mr. John Doe</div>
    <div class="contact__line">47 Thornbury Street</div>
    <div class="contact__line">New York, New York 10010</div>
    <div class="contact__line">Telephone: 212-738-4192</div>
    <div class="contact__line">Email: Casting@noraquillan.example</div>
  </address>
</div>
</body>
</html>
```